Accounting and Tax Professional

New business with a business model based on good service and bright staff,

Brin Kowalczyk B.Com CPA DIRECTOR

"Harbourline Ledger And Levy Pty Ltd"
ABN 47 583 016 728

Registered Tax Agent
PROFESSIONAL PERSONABLE TIMELY OR "PROFESSIONAL ADVICE TAILORED TO SUIT YOU"
Superannuation|Business services|Management consulting|Taxation|Software support
E Brin@HarbourlineLedgerAndLevy.example.au
WWW.HARBOURLINELEDGERANDLEVY.EXAMPLE.AU
Phone: +61 0438 715 906
24519 Corvell Ridge Road Marrowvale QLD 4352, Australia

hi, I have uploaded an .EPS logo as requested by one of the designers, let me know if this is not the right size for the business card. thanks Brin

Target Market(s)

Mainly Business clients

Industry/Entity Type

Business

Font styles to use
Serif

Colors
85acd3
3377b5

Requirements
Must have
• clean/crisp/well laid out

```html
<!DOCTYPE html>
<html lang="en">
<head>
<meta charset="utf-8">
<title>Harbourline Ledger And Levy – Business Cards</title>
<link rel="stylesheet" href="https://fonts.googleapis.com/css2?family=Exo+2:wght@400;500;600&display=swap">
<style>
  :root {
    --page: #e9ebee;
    --card-white: #ffffff;
    --card-mist: #eef0f2;
    --band-blue: #7896b7;
    --mark-blue: #6f8fb3;
    --swoosh-grey: #b9bcc0;
    --swoosh-dark: #3c3f44;
    --ink-dark: #1d2024;
    --ink-name: #6a8db5;
    --ink-light: #ffffff;
    --font-main: "Exo 2", "Segoe UI", sans-serif;
  }
  * { box-sizing: border-box; margin: 0; padding: 0; }
  html, body {
    width: 1200px; height: 900px; overflow: hidden;
    background: var(--page);
    font-family: var(--font-main);
  }
  .sheet {
    position: relative; width: 1200px; height: 900px;
  }
  .card {
    position: absolute; left: 280px;
    width: 640px; height: 366px;
    border-radius: 28px; overflow: hidden;
    background: linear-gradient(160deg, var(--card-white) 0%, var(--card-mist) 100%);
    box-shadow: 0 10px 28px rgba(30, 40, 60, 0.18);
  }
  .card--back { top: 54px; }
  .card--front { top: 474px; }
  .card__shapes { position: absolute; inset: 0; width: 100%; height: 100%; }

  /* brand block */
  .brand { position: absolute; display: flex; flex-direction: column; align-items: center; }
  .brand__dot {
    border-radius: 50%; background: var(--mark-blue);
    border: 3px solid var(--ink-dark);
  }
  .brand__name {
    color: var(--ink-dark); font-weight: 500; text-align: center;
    letter-spacing: 1px; line-height: 1.05;
  }
  .card--front .brand { right: 34px; top: 34px; width: 280px; }
  .card--front .brand__dot { width: 62px; height: 62px; margin-bottom: 10px; }
  .card--front .brand__name { font-size: 30px; }
  .card--front .brand__name small { display: block; font-size: 11.5px; letter-spacing: 0.6px; margin-top: 5px; }

  .card--back .brand { left: 190px; top: 46px; flex-direction: row; gap: 14px; }
  .card--back .brand__dot { width: 54px; height: 54px; }
  .card--back .brand__name { font-size: 28px; text-align: left; }
  .card--back .brand__name small { display: block; font-size: 10.5px; letter-spacing: 0.6px; margin-top: 4px; }

  /* person */
  .person { position: absolute; left: 40px; top: 132px; }
  .person__name {
    color: var(--ink-name); font-size: 22px; font-weight: 500; letter-spacing: 1.6px;
    text-transform: uppercase;
  }
  .person__role { color: var(--ink-dark); font-size: 14px; font-weight: 500; margin-top: 2px; letter-spacing: 0.3px; }

  .address {
    position: absolute; left: 40px; top: 268px;
    color: var(--ink-light); font-size: 13.5px; line-height: 1.55; letter-spacing: 0.5px;
    font-style: normal;
  }

  .contacts {
    position: absolute; right: 32px; top: 250px;
    list-style: none; color: var(--ink-light);
    font-size: 12.5px; letter-spacing: 0.6px;
  }
  .contacts li {
    display: flex; align-items: center; justify-content: flex-end;
    gap: 9px; height: 24px;
  }
  .contacts svg { width: 14px; height: 14px; flex: none; }
</style>
</head>
<body>
<main class="sheet">

  <!-- Back of card -->
  <section class="card card--back" aria-label="Business card back">
    <svg class="card__shapes" viewBox="0 0 640 366" preserveAspectRatio="none" aria-hidden="true">
      <path d="M0,236 C210,236 430,196 640,118 V366 H0 Z" fill="var(--band-blue)"/>
      <path d="M110,128 C300,134 450,170 560,222 C440,170 290,146 110,128 Z" fill="var(--swoosh-dark)"/>
      <path d="M150,140 C320,150 470,196 600,250 C470,200 320,162 150,140 Z" fill="var(--swoosh-grey)"/>
    </svg>
    <div class="brand">
      <span class="brand__dot"></span>
      <p class="brand__name">HARBOURLINE<small>LEDGER AND LEVY PTY LTD</small></p>
    </div>
  </section>

  <!-- Front of card -->
  <section class="card card--front" aria-label="Business card front">
    <svg class="card__shapes" viewBox="0 0 640 366" preserveAspectRatio="none" aria-hidden="true">
      <path d="M0,205 C180,245 300,282 420,266 C520,252 590,236 640,226 V366 H0 Z" fill="var(--band-blue)"/>
      <path d="M0,180 C150,204 260,250 360,262 C250,256 140,222 0,198 Z" fill="var(--swoosh-grey)"/>
    </svg>

    <div class="person">
      <h1 class="person__name">Brin Kowalczyk</h1>
      <p class="person__role">Director</p>
    </div>

    <div class="brand">
      <span class="brand__dot"></span>
      <p class="brand__name">HARBOURLINE<small>LEDGER AND LEVY PTY LTD</small></p>
    </div>

    <address class="address">24519 Corvell Ridge Road<br>Marrowvale QLD 4352</address>

    <ul class="contacts">
      <li>+61 0438 715 906
        <svg viewBox="0 0 24 24" aria-hidden="true"><path fill="#fff" d="M6.6 10.8a15.1 15.1 0 0 0 6.6 6.6l2.2-2.2c.3-.3.7-.4 1-.2 1.1.4 2.3.6 3.6.6.6 0 1 .4 1 1V20c0 .6-.4 1-1 1A17 17 0 0 1 3 4c0-.6.4-1 1-1h3.5c.6 0 1 .4 1 1 0 1.3.2 2.5.6 3.6.1.3 0 .7-.2 1z"/></svg>
      </li>
      <li>ABN 47 583 016 728
        <svg viewBox="0 0 24 24" aria-hidden="true"><rect x="7" y="2" width="10" height="20" rx="2" fill="none" stroke="#fff" stroke-width="2"/><circle cx="12" cy="18" r="1.2" fill="#fff"/></svg>
      </li>
      <li>WWW.HARBOURLINELEDGERANDLEVY.EXAMPLE.AU
        <svg viewBox="0 0 24 24" aria-hidden="true"><rect x="4" y="9" width="16" height="11" rx="1.5" fill="#fff"/><rect x="7" y="3" width="10" height="7" fill="none" stroke="#fff" stroke-width="2"/></svg>
      </li>
      <li>Brin@HarbourlineLedgerAndLevy.example.au
        <svg viewBox="0 0 24 24" aria-hidden="true"><rect x="2" y="5" width="20" height="14" rx="1.5" fill="#fff"/><path d="M3 6l9 7 9-7" fill="none" stroke="var(--band-blue)" stroke-width="1.8"/></svg>
      </li>
    </ul>
  </section>

</main>
</body>
</html>
```